Restaurant Menu Design for Meal Prep offered in a food display cooler at a local Gym

I am looking for a menu design with the following items . I would like a workable copy if possible so in the future we can change pricing on this file , or change items . This file will be uploaded on a USB drive and then plugged into a TV. Please ensure a JPEG file is included so this will also work on this TV.

Have a look at our website , www.vantorelkitchen.com for ideas for design that represent the brand appropriately.
The below are the menu items that we would need displayed along with their pricing.

BREAKFAST MEAL PREP ITEMS
Blueberry Pancakes $12.00
Full Throttle Burrito $10.95

LUNCH/DINNER MEAL PREP OPTIONS
BBQ Glazed Salmon $16.50
Cheeseburger Bowl $13.50
Chicken Alfredo $12.00
Pesto Chicken Pasta $12.00
Chicken Parmesan $13.00
Taco Bowl $14.00
Steak Bite and Green Stir Fry $12.00
Asian Chicken Teriyaki $12.00
Galloway Stir Fry $15.95

I will attach our logo below, this will need to be on the design. The "heading" (for example breakfast meal prep items and lunch/dinner meal prep options) for the menu should also be on the design.

Ive attached a couple of photos that you need to add to your design.

Target Market(s)

This will be displayed in a GYM

Industry/Entity Type

Meal Prep + Fitness Industry

Requirements
Must have
• Vantorel Logo and Photos attached
Nice to have
• Maybe incorporate something that represents working out or healthy lifestyle in design without going too overboard

```html
<!DOCTYPE html>
<html lang="en">
<head>
<meta charset="utf-8">
<title>Vantorel Healthy Kitchen – Menu</title>
<link rel="stylesheet" href="https://fonts.googleapis.com/css2?family=Ubuntu:wght@400;500;700&display=swap">
<style>
  :root {
    --wood-light: #eceae8;
    --wood-mid: #dedbd9;
    --panel-frame: #ffffff;
    --panel-fill: rgba(240, 238, 236, 0.9);
    --brand-green: #86c232;
    --text-grey: #6f7073;
    --menu-grey: #98999b;
    --pancake-tone: #e6cfb2;
    --pasta-tone: #b7b08c;
  }
  * { margin: 0; padding: 0; box-sizing: border-box; }
  html, body { width: 1200px; height: 750px; overflow: hidden; }
  body {
    position: relative;
    font-family: "Ubuntu", sans-serif;
    background: linear-gradient(100deg, var(--wood-mid) 0%, var(--wood-light) 45%, var(--wood-mid) 100%);
  }
  .menu-panel {
    position: absolute; left: 26px; top: 30px; width: 433px; height: 692px;
    border: 6px solid var(--panel-frame);
    background: var(--panel-fill);
  }
  .section-title {
    position: absolute; left: 51px;
    font-size: 36px; font-weight: 400; letter-spacing: 1.5px;
    color: var(--brand-green); line-height: 1;
  }
  .section-rule {
    position: absolute; left: 0; width: 452px; height: 2px; background: var(--brand-green);
  }
  .section-note {
    position: absolute; left: 53px; font-size: 17px; color: var(--text-grey); letter-spacing: 0.5px;
  }
  .menu-item {
    position: absolute; left: 51px; width: 384px;
    font-size: 23.5px; letter-spacing: 1px; color: var(--text-grey); line-height: 1;
  }
  .menu-item .price {
    position: absolute; left: 313px; color: var(--brand-green);
  }
  .lunch .menu-item { left: 56px; }
  .lunch .menu-item .price { left: 310px; }
  .brand-card {
    position: absolute; left: 522px; top: 277px; width: 298px; height: 195px;
    border: 6px solid var(--panel-frame);
    background: var(--panel-fill);
    text-align: center;
  }
  .brand-name {
    margin-top: 32px;
    font-size: 42px; font-weight: 700; letter-spacing: 1px;
    color: var(--brand-green); line-height: 1;
  }
  .brand-tagline {
    margin-top: 5px;
    font-size: 13.5px; font-weight: 700; color: var(--brand-green); letter-spacing: 0.2px;
  }
  .menu-word {
    margin-top: 6px;
    font-size: 70px; font-weight: 400; letter-spacing: 12px; padding-left: 12px;
    color: var(--menu-grey); line-height: 1;
  }
  .photo { position: absolute; }
  .photo-pancakes {
    left: 866px; top: 19px; width: 334px; height: 169px;
    background: var(--pancake-tone);
    border-radius: 8px;
  }
  .photo-pasta {
    left: 728px; top: 512px; width: 406px; height: 216px;
    background: var(--pasta-tone);
    border-radius: 8px;
  }
</style>
</head>
<body>

  <section class="menu-panel" aria-label="Menu items"></section>

  <section class="breakfast">
    <h2 class="section-title" style="top:47px;">Breakfast</h2>
    <div class="section-rule" style="top:80px;"></div>
    <p class="section-note" style="top:84px;">meal prep items</p>
    <p class="menu-item" style="top:133px;">Blueberry Pancakes<span class="price">$12.00</span></p>
    <p class="menu-item" style="top:171px;">Full Throttle Burrito<span class="price">$10.95</span></p>
  </section>

  <section class="lunch">
    <h2 class="section-title" style="top:269px; left:54px;">Lunch|Dinner</h2>
    <div class="section-rule" style="top:305px;"></div>
    <p class="section-note" style="top:309px; left:54px;">meal prep options</p>
    <p class="menu-item" style="top:358px;">Cheeseburger Bowl<span class="price">$13.50</span></p>
    <p class="menu-item" style="top:394px;">Chicken Alfredo<span class="price">$12.00</span></p>
    <p class="menu-item" style="top:430px;">Pesto Chicken Pasta<span class="price">$12.00</span></p>
    <p class="menu-item" style="top:466px;">BBQ Glazed Salmon<span class="price">$16.50</span></p>
    <p class="menu-item" style="top:502px;">Chicken Parmesan<span class="price">$13.00</span></p>
    <p class="menu-item" style="top:538px;">Taco Bowl<span class="price">$14.00</span></p>
    <p class="menu-item" style="top:574px;">Asian Chicken Teriyaki<span class="price">$12.00</span></p>
    <p class="menu-item" style="top:610px;">Galloway Stir Fry<span class="price">$15.95</span></p>
    <p class="menu-item" style="top:646px;">Steak Bite and Green<span class="price">$12.00</span></p>
    <p class="menu-item" style="top:682px;">Stir Fry</p>
  </section>

  <header class="brand-card">
    <h1 class="brand-name">VANTOREL</h1>
    <p class="brand-tagline">HEALTHY KITCHEN | MEAL PREP</p>
    <p class="menu-word">MENU</p>
  </header>

  <div class="photo photo-pancakes" role="img" aria-label="Photo of blueberry pancakes on a white plate"></div>
  <div class="photo photo-pasta" role="img" aria-label="Photo of pesto chicken pasta in a white bowl"></div>

</body>
</html>
```